GlowRun Fundraiser

I am looking for a fresh design for the 10th annual GlowRun fundraiser. Green and blue colors need to be incorporated . I attached the current flyer. I would like this flyer for September 20, 2020. This is a fundraiser to help find a cure for NF, nuerofibromatosis.
Updates

We are looking for a fresh look for the 10th annual event

Target Market(s)

Families and individuals of surrounding areas

Colors
0255a3
add136

Requirements
Must have
• Blue and green colors. It is the 10th annual. The logos of RQ CENTER and children’s hospital logo that are shown on the previous flyer I attached
Nice to have
• Eye catching

```html
<!DOCTYPE html>
<html lang="en">
<head>
<meta charset="utf-8">
<title>GlowRun Fundraiser</title>
<link rel="stylesheet" href="https://fonts.googleapis.com/css2?family=Montserrat:wght@400;800&family=Roboto:wght@300;500&family=Roboto+Condensed:wght@700&family=Oswald:wght@600&display=swap">
<style>
  :root {
    --blue: #0255a3;
    --green: #add136;
    --gray: #7a7a7a;
    --navy: #0d2a52;
  }
  * { margin: 0; padding: 0; box-sizing: border-box; }
  html, body { width: 927px; height: 1200px; overflow: hidden; background: #fff; }
  .flyer { position: relative; width: 927px; height: 1200px; overflow: hidden; font-family: "Montserrat", sans-serif; }
  .backdrop { position: absolute; inset: 0; }

  .event-mark { position: absolute; left: 40px; top: 14px; width: 300px; text-align: center; }
  .event-mark .edition { font-family: "Oswald", sans-serif; font-weight: 600; font-size: 26px; letter-spacing: 4px; color: var(--blue); line-height: 1.1; }
  .event-mark .name { font-family: "Oswald", sans-serif; font-weight: 600; font-size: 84px; line-height: 1; color: var(--navy); }

  .headline { position: absolute; left: 0; width: 848px; text-align: center; color: var(--blue); white-space: nowrap; }
  .join { top: 198px; font-weight: 800; font-size: 108px; line-height: 1; }
  .support { top: 294px; font-weight: 400; font-size: 55px; line-height: 1; letter-spacing: 1px; }
  .beneficiary { font-weight: 400; font-size: 34px; line-height: 1; letter-spacing: 1px; }
  .beneficiary.one { top: 357px; }
  .beneficiary.two { top: 403px; }

  .details { position: absolute; right: 143px; top: 592px; text-align: right; color: var(--green); font-family: "Roboto Condensed", sans-serif; font-weight: 700; line-height: 1; white-space: nowrap; }
  .details .date { font-size: 52px; }
  .details .time { font-size: 44px; margin-top: 8px; }
  .details .venue { font-size: 44px; margin-top: 7px; }
  .details .address { font-size: 29px; margin-top: 6px; line-height: 1.05; }

  .highlights { position: absolute; right: 116px; top: 824px; color: var(--gray); font-family: "Roboto", sans-serif; font-weight: 500; font-size: 43px; white-space: nowrap; }
  .activities { position: absolute; list-style: none; color: var(--gray); font-family: "Roboto Condensed", sans-serif; font-weight: 700; font-size: 25px; letter-spacing: 0.5px; white-space: nowrap; }
  .activities li { height: 38px; }
  .activities li::before { content: "\2022"; font-size: 11px; vertical-align: middle; margin-right: 3px; color: var(--green); }
  .activities.left { left: 224px; top: 882px; }
  .activities.right { left: 500px; top: 880px; }

  .partner-mark { position: absolute; left: 24px; color: var(--navy); font-weight: 800; text-align: center; width: 110px; line-height: 1.05; }
  .partner-mark.hospital { top: 1054px; font-size: 14px; }
  .partner-mark.center { top: 1110px; font-size: 24px; }

  .contact-title { position: absolute; right: 34px; top: 1084px; color: var(--gray); font-family: "Roboto", sans-serif; font-weight: 300; font-size: 44px; white-space: nowrap; }
  .contacts { position: absolute; top: 1138px; color: var(--gray); font-family: "Roboto", sans-serif; font-weight: 300; font-size: 18px; line-height: 21px; white-space: nowrap; }
  .contacts.left { left: 351px; }
  .contacts.right { left: 631px; }
</style>
</head>
<body>
<main class="flyer">
  <svg class="backdrop" width="927" height="1200" viewBox="0 0 927 1200" aria-hidden="true">
    <defs>
      <linearGradient id="paper" x1="0" y1="0" x2="0" y2="1">
        <stop offset="0.45" stop-color="#ffffff"/>
        <stop offset="1" stop-color="#ebebeb"/>
      </linearGradient>
      <linearGradient id="tealSweep" x1="0" y1="0" x2="1" y2="1">
        <stop offset="0" stop-color="#1ec9c6"/>
        <stop offset="1" stop-color="#127b78"/>
      </linearGradient>
      <linearGradient id="tealSide" x1="0" y1="0" x2="1" y2="0">
        <stop offset="0" stop-color="#127b78"/>
        <stop offset="1" stop-color="#18b9b1"/>
      </linearGradient>
      <linearGradient id="orangeBand" x1="0" y1="0" x2="1" y2="0">
        <stop offset="0" stop-color="#f2852c"/>
        <stop offset="0.45" stop-color="#fbbd3f"/>
        <stop offset="1" stop-color="#f2852c"/>
      </linearGradient>
    </defs>
    <rect width="927" height="1200" fill="url(#paper)"/>
    <path d="M540 0 L700 0 C620 80 470 148 330 176 C430 122 500 62 540 0 Z" fill="url(#orangeBand)"/>
    <path d="M0 0 L565 0 C450 95 300 172 190 207 C120 212 55 202 0 186 Z" fill="url(#tealSweep)"/>
    <path d="M0 692 C200 560 500 455 825 502 L825 516 C560 480 260 555 0 606 Z" fill="url(#orangeBand)"/>
    <path d="M927 228 C858 330 818 480 818 615 C818 790 868 940 927 992 Z" fill="url(#tealSide)"/>
    <path d="M0 807 C150 900 262 1050 300 1200 L0 1200 Z" fill="url(#tealSweep)"/>
    <path d="M0 870 C110 960 190 1080 215 1200 L0 1200 Z" fill="#127b78" opacity="0.35"/>
  </svg>

  <div class="event-mark">
    <div class="edition">10TH ANNUAL</div>
    <div class="name">GlowRun</div>
  </div>

  <h1 class="headline join">JOIN US</h1>
  <p class="headline support">IN SUPPORT</p>
  <p class="headline beneficiary one">RIVERSIDE CHILDREN'S HOSPITAL</p>
  <p class="headline beneficiary two">LAKEVIEW UNIVERSITY RQ CENTER</p>

  <section class="details">
    <p class="date">SUNDAY, SEPT 20 2020</p>
    <p class="time">12PM - 6PM</p>
    <p class="venue">MAPLE COUNTY FAIR GROUNDS</p>
    <p class="address">512 W. ORCHARD ROAD, MILLBROOK,<br>IL 62400</p>
  </section>

  <p class="highlights">FOOD, DRINKS, MUSIC &amp; FUN</p>
  <ul class="activities left">
    <li>KID GAMES</li>
    <li>BOUNCE HOUSE</li>
    <li>FACE PAINTING</li>
  </ul>
  <ul class="activities right">
    <li>SILENT &amp; LIVE AUCTION</li>
    <li>12-2 WALK-IN APPOINTMENTS</li>
    <li>CHILDREN SPECIAL BY HARLOW</li>
  </ul>

  <p class="partner-mark hospital">Riverside Children's</p>
  <p class="partner-mark center">RQ CENTER</p>

  <p class="contact-title">PLEASE CONTACT:</p>
  <p class="contacts left">Dana Wells - (555) 201 - 4417<br>Kara Bennett - (555) 318 - 2290</p>
  <p class="contacts right">Nora Fields - (555) 742 - 6081<br>Jill Parsons - (555) 463 - 9125</p>
</main>
</body>
</html>
```